Flyer Design Project for our Parenting Psychologists at the Bright Harbour Wellbeing Clinic

At the Bright Harbour Wellbeing Clinic we have expert Parenting Psychologists.

Parenting Psychologists provide practical, step by step assistance to parents who are struggling with their children's behavioural and emotional problems.

We need a DL size brochure that will be appealing to parents. The brochure will be on show in schools, kindergartens and GP clinics.

In terms of style it will be in line with our website and stationery that I will attach.

www.brightharbourwellbeing.com.au
Updates

Hi Everyone,
Thanks for putting forward your proposals, there are a couple there that I am very interested in. I am looking to see if there is a way that I can change my brief to guaranteed as I am definitely going to be using one of the designs for sure.
I have emailed ArtFolkly and as soon as I get an answer I will change it if I can.
If anyone out there already knows the answer please let me know :-)
Thanks,
Marnie.

Hi Again,

I worked it out myself!!

I have now changed this to a committed project.

Kind regards,
Marnie.

Reason: I have 46 designs now and need more time to work out which is best!

Target Market(s)

The target will be educated professional parents motivated to get professional help. And doctors and teachers who will pass on the brochures 2 parents

Industry/Entity Type

Health

Requirements
Must have
• I want one DL size brochure. Back and front.

We need text (below) and our contact details. Our logo.

9362 4158
Suite 1, 2071 Pellbrook Rd, Ferndale Heights 3109

Text:
Parents want the best for their kids. They want kids that are happy, healthy and well behaved.

So why is it so hard? Parents of toddlers, primary schoolers and teenagers alike say that they are frustrated by constant nagging, bribing and yelling, they don't know what to try next. Some parents worry that their children are unhappy. Struggling at school, not making friends or coping with bigger problems.

The good news is that getting your children to behave more co-operatively doesn't need to be difficult or mysterious. We all know that kids don't come with manuals, but there are skills every parent can learn to make parenting easier. In a few sessions with a Parenting Psychologist, you will receive step by step guidance in how to talk to your children in a way that will be much more effective getting them to behave in a respectful and co-operative way around the home and in public. You will learn how to help your child cope with problems they are going through. They can help you reconnect with your kids so you can enjoy being a parent again.

Nice to have
• Themes consistent with our website
and letterhead, business cards. I will attach these.
Should not have
• I don't want it to look too cluttered so if the text I have provided up above looks too crowded then I will edit it.

```html
<!DOCTYPE html>
<html lang="en">
<head>
<meta charset="utf-8">
<title>Bright Harbour Wellbeing Clinic – Parenting Psychologists DL Brochure</title>
<link href="https://fonts.googleapis.com/css2?family=Caladea:ital,wght@0,400;0,700&display=swap" rel="stylesheet">
<style>
  :root {
    --stage: #0d0d0d;
    --panel-top: #bfe5f6;
    --panel-mid: #dcf1fa;
    --panel-bottom: #ffffff;
    --header-blue: #3f93cf;
    --header-light: #7fc0e6;
    --brand-white: #ffffff;
    --text-teal: #2a8c95;
    --heading-green: #1d6f62;
    --footer-green: #1f6a58;
    --echo: rgba(255, 255, 255, 0.55);
    --strip-1: #6f9db2;
    --strip-2: #7fc6cb;
    --strip-3: #73a8a5;
    --strip-4: #8f9fab;
    --photo-grass: #6f9d45;
    --photo-light: #cfe4b0;
    --photo-warm: #d9a08a;
  }
  * { box-sizing: border-box; margin: 0; padding: 0; }
  html, body { width: 1200px; height: 1000px; overflow: hidden; }
  body {
    background: var(--stage);
    font-family: "Caladea", "Cambria", Georgia, serif;
    position: relative;
  }
  .brochure {
    position: absolute;
    left: 180px;
    top: 70px;
    display: flex;
    gap: 30px;
  }
  .panel {
    position: relative;
    width: 410px;
    height: 860px;
    background: linear-gradient(180deg, var(--panel-top) 0%, var(--panel-mid) 55%, var(--panel-bottom) 92%);
    overflow: hidden;
  }

  .panel-header {
    position: absolute;
    left: 0; top: 0;
    width: 100%;
    height: 200px;
    background: linear-gradient(180deg, var(--header-light) 0%, var(--header-blue) 100%);
    clip-path: polygon(0 0, 100% 0, 100% 78%, 0 100%);
  }
  .brand {
    position: absolute;
    left: 28px;
    top: 54px;
    display: flex;
    align-items: center;
    gap: 18px;
  }
  .brand-dot {
    width: 62px; height: 62px;
    border-radius: 50%;
    background: var(--heading-green);
    flex: none;
  }
  .brand-name {
    color: var(--brand-white);
    font-size: 25px;
    font-weight: 400;
    letter-spacing: 3px;
    line-height: 1.08;
    text-transform: uppercase;
  }

  .intro {
    position: absolute;
    left: 24px; top: 222px;
    width: 330px;
    color: var(--text-teal);
    font-size: 19px;
    line-height: 1.5;
  }
  .intro strong { color: var(--heading-green); }

  .headline-group { position: absolute; left: 24px; top: 332px; width: 390px; }
  .headline {
    color: var(--heading-green);
    font-size: 36px;
    font-weight: 400;
    white-space: nowrap;
  }
  .headline-echo {
    color: var(--echo);
    font-size: 32px;
    white-space: nowrap;
    margin-top: -8px;
    margin-left: 48px;
  }

  .body-copy {
    position: absolute;
    left: 24px;
    color: var(--text-teal);
  }
  .panel-front .body-copy { top: 470px; width: 370px; font-size: 18.5px; line-height: 1.62; }
  .panel-back .body-copy { top: 345px; width: 370px; font-size: 17px; line-height: 1.5; }

  .contact {
    position: absolute;
    left: 0; bottom: 58px;
    width: 100%;
    text-align: center;
    color: var(--footer-green);
  }
  .contact-address { font-size: 16px; }
  .contact-phone { font-size: 19px; margin-top: 4px; }
  .contact-web { font-size: 19px; margin-top: 10px; }

  .colour-strip {
    position: absolute;
    left: 0; bottom: 0;
    width: 100%;
    height: 36px;
    display: flex;
  }
  .colour-strip span { flex: 1; }
  .colour-strip span:nth-child(1) { background: var(--strip-1); flex: 0.8; }
  .colour-strip span:nth-child(2) { background: var(--strip-2); }
  .colour-strip span:nth-child(3) { background: var(--strip-3); }
  .colour-strip span:nth-child(4) { background: var(--strip-4); flex: 0.8; }

  .family-photo {
    position: absolute;
    left: 0; top: 0;
    width: 100%;
    height: 330px;
    background:
      radial-gradient(ellipse at 55% 55%, var(--photo-warm) 0%, rgba(217,160,138,0) 38%),
      linear-gradient(180deg, var(--photo-light) 0%, var(--photo-grass) 60%, #8fb866 100%);
    -webkit-mask-image: radial-gradient(ellipse 78% 72% at 50% 45%, #000 62%, transparent 100%);
    mask-image: radial-gradient(ellipse 78% 72% at 50% 45%, #000 62%, transparent 100%);
  }
</style>
</head>
<body>
  <main class="brochure">
    <section class="panel panel-front">
      <div class="panel-header"></div>
      <div class="brand">
        <span class="brand-dot"></span>
        <span class="brand-name">Bright Harbour<br>Wellbeing<br>Clinic</span>
      </div>

      <p class="intro">Parents want the best for their kids. They want kids that are <strong>happy</strong>, <strong>healthy</strong> and <strong>well behaved</strong>.</p>

      <div class="headline-group">
        <h1 class="headline">So why is it so hard?</h1>
        <p class="headline-echo" aria-hidden="true">So why is it so hard?</p>
      </div>

      <p class="body-copy">Parents of toddlers, primary schoolers and teenagers alike say that they are frustrated by constant nagging, bribing and yelling, they don't know what to try next. Some parents worry that their children are unhappy. Struggling at school, not making friends or coping with bigger problems.</p>

      <footer class="contact">
        <p class="contact-address">Suite 1, 2071 Pellbrook Rd, Ferndale Heights 3109</p>
        <p class="contact-phone">9362 4158</p>
        <p class="contact-web">www.brightharbourwellbeing.com.au</p>
      </footer>
      <div class="colour-strip"><span></span><span></span><span></span><span></span></div>
    </section>

    <section class="panel panel-back">
      <div class="family-photo" role="img" aria-label="Photo of a mother smiling at her toddler on a picnic blanket in a sunny park"></div>

      <p class="body-copy">The good news is that getting your children to behave more co-operatively doesn't need to be difficult or mysterious. We all know that kids don't come with manuals, but there are skills every parent can learn to make parenting easier. In a few sessions with a Parenting Psychologist, you will receive step by step guidance in how to talk to your children in a way that will be much more effective getting them to behave in a respectful and co-operative way around the home and in public. You will learn how to help your child cope with problems they are going through. They can help you reconnect with your kids so you can enjoy being a parent again.</p>

      <footer class="contact">
        <p class="contact-address">Suite 1, 2071 Pellbrook Rd, Ferndale Heights 3109</p>
        <p class="contact-phone">9362 4158</p>
        <p class="contact-web">www.brightharbourwellbeing.com.au</p>
      </footer>
      <div class="colour-strip"><span></span><span></span><span></span><span></span></div>
    </section>
  </main>
</body>
</html>
```